Logo and 1 page Flyer for Meadowlark Fund

We need a logo and a 1 single page flyer for an Investment Fund we'll distribute worldwide. It'a Meadowlark Fund that will give a return also to the poorest people in the world. Details inside. We give just an idea (based on a previous flyer we had here) with the attached draft. Anyone can figure out how to make its own. NOTE: TQV is our company's logo.

Target Market(s)

Investors

Industry/Entity Type

Finance And Accounting

Logo Text

KELP Kindred Open Grow Fund

Font styles to use
Serif

Colors
00a990

Requirements
Must have
• A logo you choose which should be:
• - Elegant
• - Innovative
• - Crypto evoking (Company launching is a cripto company)
• - Hi tech
Nice to have
• We have sent you all materials to be able to understand:
• 1. A draft of how we would like the texts to come out. Don't use this (we're already using with other texts), ,but see the evidence of Logo, Slogan, and the 3 main characteristics. Also notice very well that is very elegant. Use a real light on color, make it as shining as you can. It must be a sort of shining green, expressing Hope, Beauty, Well being
• 2. The logo for TQV that is the company launching the project. In draft you see on low left. You can put wherever you feel right
• 3. All texts are on draft to be seen, and on word to be used. You can choose font and dimensions as you prefer
• 4. We've given you logo we have for PLOM. If you feel, you can use in the line where we talk about it or place somewhere. Not mandatory
Should not have
• Funny things; too commercial style; unprofessional aspect

```html
<!DOCTYPE html>
<html lang="en">
<head>
<meta charset="utf-8">
<title>KELP – Kindred Open Grow Fund</title>
<link rel="stylesheet" href="https://fonts.googleapis.com/css2?family=Playfair+Display:wght@700;900&family=Source+Serif+4:wght@400;600;700&display=swap">
<style>
  :root {
    --navy: #13166a;
    --night: #05061a;
    --shine-green: #00a990;
    --shine-green-light: #2fd6b8;
    --deep-green: #00806d;
    --ink-grey: #4a4a4a;
    --paper: #ffffff;
    --paper-mint: #dff3ef;
  }
  * { margin: 0; padding: 0; box-sizing: border-box; }
  html, body { width: 928px; height: 1200px; overflow: hidden; background: var(--paper); }
  .flyer {
    position: relative; width: 928px; height: 1200px; overflow: hidden;
    font-family: "Source Serif 4", serif;
  }

  /* Hero */
  .hero { position: absolute; left: 0; top: 0; width: 928px; height: 728px; }
  .hero-photo {
    position: absolute; inset: 0;
    background:
      radial-gradient(ellipse 170px 140px at 195px 510px, rgba(235,225,200,0.55), transparent 70%),
      radial-gradient(ellipse 240px 220px at 120px 260px, rgba(40,150,190,0.45), transparent 70%),
      linear-gradient(180deg, #0c1030 0%, #1a2466 45%, #0d1440 75%, var(--night) 100%);
  }
  .hero-shapes { position: absolute; inset: 0; }
  .headline-text {
    font-family: "Playfair Display", serif; font-weight: 900; fill: var(--paper);
  }
  .hero-lede {
    position: absolute; right: 98px; top: 478px; width: 420px;
    text-align: right; color: var(--paper);
    font-size: 22px; line-height: 29px; font-weight: 400;
  }

  /* Lower section */
  .features-band {
    position: absolute; left: 0; top: 728px; width: 928px; height: 472px;
    background: linear-gradient(180deg, var(--paper-mint) 0%, var(--paper) 45%, #eef8f6 100%);
  }
  .feature-title {
    position: absolute; left: 84px;
    font-family: "Playfair Display", serif; font-weight: 700;
    color: var(--deep-green); font-size: 29px; line-height: 34px;
  }
  .feature-title::after {
    content: ""; position: absolute; left: 0; bottom: -4px;
    width: 80px; height: 2px; background: var(--shine-green);
  }
  .feature-text {
    position: absolute; left: 84px; width: 440px;
    color: var(--ink-grey); font-size: 17px; line-height: 22.5px;
  }

  .brand-mark { position: absolute; left: 649px; top: 812px; }
  .brand-lockup { position: absolute; left: 578px; top: 998px; width: 302px; text-align: center; }
  .brand-name {
    font-family: "Playfair Display", serif; font-weight: 900;
    color: var(--shine-green); font-size: 112px; line-height: 104px; letter-spacing: 3px;
  }
  .brand-tagline {
    margin-top: 2px; font-family: "Playfair Display", serif; font-weight: 900;
    color: var(--shine-green); font-size: 18.5px; letter-spacing: 0.3px;
  }

  .footer-tab { position: absolute; left: 0; top: 1128px; width: 440px; height: 72px; }
  .footer-url {
    position: absolute; left: 84px; top: 1137px;
    color: var(--paper); font-size: 26px; font-weight: 600; letter-spacing: 0.3px;
  }
</style>
</head>
<body>
<main class="flyer">
  <section class="hero">
    <div class="hero-photo" role="img" aria-label="Dark blue blurred trading screen with a gold crypto coin standing on a desk"></div>
    <svg class="hero-shapes" width="928" height="728" viewBox="0 0 928 728" aria-hidden="true">
      <polygon points="0,12 928,0 928,728 512,728" fill="var(--navy)" opacity="0.78"/>
      <polygon points="760,0 928,0 928,215" fill="#2a3a8a" opacity="0.5"/>
      <rect x="446" y="465" width="384" height="3" fill="var(--paper)"/>
    </svg>
    <h1>
      <svg class="hero-shapes" width="928" height="728" viewBox="0 0 928 728" aria-label="Raise the poor surfing with us">
        <text class="headline-text" x="830" y="168" text-anchor="end" font-size="74" textLength="397" lengthAdjust="spacingAndGlyphs">RAISE THE</text>
        <text class="headline-text" x="830" y="296" text-anchor="end" font-size="146" textLength="397" lengthAdjust="spacingAndGlyphs">POOR</text>
        <text class="headline-text" x="830" y="380" text-anchor="end" font-size="90" textLength="397" lengthAdjust="spacingAndGlyphs">SURFING</text>
        <text class="headline-text" x="830" y="442" text-anchor="end" font-size="60" textLength="397" lengthAdjust="spacing">W I T H&#160;&#160;U S</text>
      </svg>
    </h1>
    <p class="hero-lede">With KELP you achieve sound<br>return on your investment.<br>And you help needy ones to<br>obtain real help in their life.</p>
  </section>

  <section class="features-band"></section>

  <h2 class="feature-title" style="top:800px">Better RETURN</h2>
  <p class="feature-text" style="top:844px">Using PLOM – Highly Advanced&nbsp; Trading System.<br>A breakthrough in money management</p>
  <h2 class="feature-title" style="top:905px">For ANYONE</h2>
  <p class="feature-text" style="top:949px">For those who can invest.&nbsp; And for those Who<br>have no money to survive.</p>
  <h2 class="feature-title" style="top:1010px">Money and HEARTH</h2>
  <p class="feature-text" style="top:1054px">To have a return that Warms you and others.</p>

  <svg class="brand-mark" width="160" height="160" viewBox="0 0 160 160" aria-hidden="true">
    <defs>
      <radialGradient id="shine" cx="0.35" cy="0.3" r="0.8">
        <stop offset="0" stop-color="var(--shine-green-light)"/>
        <stop offset="1" stop-color="var(--shine-green)"/>
      </radialGradient>
    </defs>
    <circle cx="80" cy="80" r="76" fill="url(#shine)"/>
  </svg>
  <div class="brand-lockup">
    <div class="brand-name">KELP</div>
    <div class="brand-tagline">Kindred Open Grow Fund</div>
  </div>

  <svg class="footer-tab" width="440" height="72" viewBox="0 0 440 72" aria-hidden="true">
    <defs>
      <linearGradient id="tabFill" x1="0" y1="0" x2="1" y2="0">
        <stop offset="0" stop-color="var(--deep-green)"/>
        <stop offset="1" stop-color="var(--shine-green)"/>
      </linearGradient>
    </defs>
    <path d="M0,0 H330 C385,0 420,30 438,72 H0 Z" fill="url(#tabFill)"/>
  </svg>
  <div class="footer-url">www.tqvf.io</div>
</main>
</body>
</html>
```